Youth organisation needs design work for awards booklet

We are from The Lantern Corps in Singapore, and we need design work for an awards booklet for one of our most prestigious awards, the Keystone Medal. The recipients are sixteen year old teenagers. This booklet will comprise of the list of the recipients, congratulatory notes and stories from some of the recipients. This booklet will be printed for each of the recipient and his guests to keep as a remembrance. We are looking for dual or tri-colour scheme, with bronze being one of the colours.
Updates

Target Market(s)

Recipients of the Award, their parents, school Principals and teachers

Requirements
Must have
• We are looking to have around 16 designed pages, including front and back cover. Size of the booklet is:
Closed - W100mm x H210mm; Opened - W200mm x H210mm
Cover page - picture of the Award
Page 3 - programme highlights
Page 4-5 - picture of the Award and description of the Award
Page 6-7 - Testimonials
Page 8-14 - List of recipients (to be provided upon confirmation of designer)
Page 15 - blank page or acknowledgments page
Back Cover - LC Logo and contact details
(Refer to previous years' booklets for reference)

Designers can submit just the cover pages as well as 1 sample inner page to get a sense of the overall style of design during the selection round.
Nice to have
• Clean, prestigious/premium look

```html
<!DOCTYPE html>
<html lang="en">
<head>
<meta charset="utf-8">
<title>Testimonials – Keystone Medal Booklet</title>
<link href="https://fonts.googleapis.com/css2?family=Montserrat:ital,wght@0,600;0,700;0,800;1,600&family=Questrial&display=swap" rel="stylesheet">
<style>
  :root {
    --paper: #dcdcdc;
    --ink-dark: #0d0d0d;
    --ink-mid: #262626;
    --gold: #d9b75e;
    --gold-light: #f3dc97;
    --gold-deep: #a9853a;
    --text: #f2f2f2;
    --fold: #bfbfbf;
  }
  * { box-sizing: border-box; margin: 0; padding: 0; }
  html, body { width: 1147px; height: 1200px; overflow: hidden; background: var(--paper); }
  .canvas { position: relative; width: 1147px; height: 1200px; }

  .spread {
    position: absolute; left: 53px; top: 51px; width: 1043px; height: 1096px; overflow: hidden;
    background:
      radial-gradient(circle at 576px 612px, rgba(255,220,140,.28) 0, rgba(255,220,140,0) 30px),
      radial-gradient(circle at 403px 200px, rgba(255,220,140,.22) 0, rgba(255,220,140,0) 26px),
      linear-gradient(180deg, var(--ink-dark) 0%, var(--ink-mid) 55%, #1c1c1c 78%, var(--ink-dark) 100%);
  }
  .facet-band { position: absolute; left: 0; width: 100%; }
  .facet-band--top {
    top: 0; height: 200px;
    background: linear-gradient(180deg, rgba(60,60,60,.7) 0%, rgba(40,36,28,.35) 55%, rgba(0,0,0,0) 100%);
  }
  .facet-band--bottom {
    bottom: 0; height: 190px;
    background: linear-gradient(0deg, rgba(10,10,10,.9) 0%, rgba(70,58,34,.35) 55%, rgba(0,0,0,0) 100%);
  }

  .fold-line {
    position: absolute; left: 573px; top: 34px; height: 1132px;
    border-left: 1px dashed var(--fold);
  }

  .page-title {
    position: absolute; left: 167px; top: 216px;
    font-family: "Montserrat", sans-serif; font-weight: 800; font-size: 37px; letter-spacing: 0;
    background: linear-gradient(90deg, #fff6dc 0%, var(--gold) 35%, #fff3cf 60%, var(--gold-deep) 100%);
    -webkit-background-clip: text; background-clip: text; color: transparent;
  }

  .testimonial {
    position: absolute; width: 418px; height: 302px;
    border: 2px solid var(--gold); border-top: none;
    text-align: center; color: var(--text);
  }
  .testimonial::before, .testimonial::after {
    content: ""; position: absolute; top: 0; height: 2px; background: var(--gold);
  }
  .testimonial::before { left: -2px; width: 100px; }
  .testimonial::after { right: -2px; width: 106px; }
  .testimonial--a { left: 105px; top: 306px; }
  .testimonial--b { left: 627px; top: 306px; }
  .testimonial--c { left: 105px; top: 662px; }
  .testimonial--d { left: 627px; top: 662px; }

  .testimonial__name {
    position: absolute; left: 0; right: 0; top: -13px;
    font-family: "Montserrat", sans-serif; font-weight: 800; font-size: 18.5px; letter-spacing: 1px;
    color: var(--gold);
  }
  .testimonial__unit {
    position: absolute; left: 0; right: 0; top: 11px;
    font-family: "Montserrat", sans-serif; font-weight: 700; font-size: 13px; letter-spacing: 1px;
  }
  .testimonial__org {
    position: absolute; left: 0; right: 0; top: 27px;
    font-family: "Montserrat", sans-serif; font-style: italic; font-weight: 600; font-size: 12.5px;
    letter-spacing: 1px; line-height: 15.5px; color: #e6e6e6;
  }
  .testimonial__quote {
    position: absolute; left: 34px; width: 348px; top: 74px;
    font-family: "Questrial", sans-serif; font-size: 14.6px; line-height: 18.4px;
    letter-spacing: -0.45px; text-align: left;
  }
  .quote-line {
    display: block; white-space: nowrap;
    text-align: justify; text-align-last: justify;
  }
  .quote-line--last { text-align-last: left; }
  .quote-mark { display: inline-block; width: 18px; height: 11px; vertical-align: 0; }
  .quote-mark--open { margin-right: 6px; }
  .quote-mark--close { margin-left: 8px; }
</style>
</head>
<body>
<div class="canvas">
  <div class="spread">
    <div class="facet-band facet-band--top" role="img" aria-label="Dark faceted crystal shards with bronze-gold edge highlights"></div>
    <div class="facet-band facet-band--bottom" role="img" aria-label="Dark faceted crystal shards with bronze-gold edge highlights"></div>
  </div>

  <h1 class="page-title">TESTIMONIALS</h1>

  <article class="testimonial testimonial--a">
    <h2 class="testimonial__name">Mr Lim Jun Hao</h2>
    <p class="testimonial__unit">7th Northvale Company</p>
    <p class="testimonial__org">Northvale Secondary School<br>Northvale Grace Church (Lutheran)</p>
    <p class="testimonial__quote">
      <span class="quote-line"><svg class="quote-mark quote-mark--open" viewBox="0 0 18 11"><polygon points="0,0 5,0 9,11 4,11" fill="#d9b75e"/><polygon points="8,0 13,0 17,11 12,11" fill="#d9b75e"/></svg>Since the start of my journey in The Lantern Corps,</span>
      <span class="quote-line">my batchmates have always motivated me to press</span>
      <span class="quote-line">on and work hard towards every goal we set our</span>
      <span class="quote-line">sights on. It is through journeying with them and</span>
      <span class="quote-line">my Officers that I have learnt valuable lessons of</span>
      <span class="quote-line">perseverance, self-discipline, selflessness and to care</span>
      <span class="quote-line">for others. Resillience is one of the most important</span>
      <span class="quote-line">values I have gained, as the fair share od mistakes</span>
      <span class="quote-line">I made along the way taught me that the journey</span>
      <span class="quote-line">was far more important than the result because this</span>
      <span class="quote-line quote-line--last">gave us the opportunity to become better.<svg class="quote-mark quote-mark--close" viewBox="0 0 18 11"><polygon points="4,0 9,0 5,11 0,11" fill="#d9b75e"/><polygon points="13,0 18,0 14,11 9,11" fill="#d9b75e"/></svg></span>
    </p>
  </article>

  <article class="testimonial testimonial--b">
    <h2 class="testimonial__name">Mr Lim Jun Hao</h2>
    <p class="testimonial__unit">7th Northvale Company</p>
    <p class="testimonial__org">Northvale Secondary School<br>Northvale Grace Church (Lutheran)</p>
    <p class="testimonial__quote">
      <span class="quote-line"><svg class="quote-mark quote-mark--open" viewBox="0 0 18 11"><polygon points="0,0 5,0 9,11 4,11" fill="#d9b75e"/><polygon points="8,0 13,0 17,11 12,11" fill="#d9b75e"/></svg>Since the start of my journey in The Lantern Corps,</span>
      <span class="quote-line">my batchmates have always motivated me to press</span>
      <span class="quote-line">on and work hard towards every goal we set our</span>
      <span class="quote-line">sights on. It is through journeying with them and</span>
      <span class="quote-line">my Officers that I have learnt valuable lessons of</span>
      <span class="quote-line">perseverance, self-discipline, selflessness and to care</span>
      <span class="quote-line">for others. Resillience is one of the most important</span>
      <span class="quote-line">values I have gained, as the fair share od mistakes</span>
      <span class="quote-line">I made along the way taught me that the journey</span>
      <span class="quote-line">was far more important than the result because this</span>
      <span class="quote-line quote-line--last">gave us the opportunity to become better.<svg class="quote-mark quote-mark--close" viewBox="0 0 18 11"><polygon points="4,0 9,0 5,11 0,11" fill="#d9b75e"/><polygon points="13,0 18,0 14,11 9,11" fill="#d9b75e"/></svg></span>
    </p>
  </article>

  <article class="testimonial testimonial--c">
    <h2 class="testimonial__name">Mr Lim Jun Hao</h2>
    <p class="testimonial__unit">7th Northvale Company</p>
    <p class="testimonial__org">Northvale Secondary School<br>Northvale Grace Church (Lutheran)</p>
    <p class="testimonial__quote">
      <span class="quote-line"><svg class="quote-mark quote-mark--open" viewBox="0 0 18 11"><polygon points="0,0 5,0 9,11 4,11" fill="#d9b75e"/><polygon points="8,0 13,0 17,11 12,11" fill="#d9b75e"/></svg>Since the start of my journey in The Lantern Corps,</span>
      <span class="quote-line">my batchmates have always motivated me to press</span>
      <span class="quote-line">on and work hard towards every goal we set our</span>
      <span class="quote-line">sights on. It is through journeying with them and</span>
      <span class="quote-line">my Officers that I have learnt valuable lessons of</span>
      <span class="quote-line">perseverance, self-discipline, selflessness and to care</span>
      <span class="quote-line">for others. Resillience is one of the most important</span>
      <span class="quote-line">values I have gained, as the fair share od mistakes</span>
      <span class="quote-line">I made along the way taught me that the journey</span>
      <span class="quote-line">was far more important than the result because this</span>
      <span class="quote-line quote-line--last">gave us the opportunity to become better.<svg class="quote-mark quote-mark--close" viewBox="0 0 18 11"><polygon points="4,0 9,0 5,11 0,11" fill="#d9b75e"/><polygon points="13,0 18,0 14,11 9,11" fill="#d9b75e"/></svg></span>
    </p>
  </article>

  <article class="testimonial testimonial--d">
    <h2 class="testimonial__name">Mr Lim Jun Hao</h2>
    <p class="testimonial__unit">7th Northvale Company</p>
    <p class="testimonial__org">Northvale Secondary School<br>Northvale Grace Church (Lutheran)</p>
    <p class="testimonial__quote">
      <span class="quote-line"><svg class="quote-mark quote-mark--open" viewBox="0 0 18 11"><polygon points="0,0 5,0 9,11 4,11" fill="#d9b75e"/><polygon points="8,0 13,0 17,11 12,11" fill="#d9b75e"/></svg>Since the start of my journey in The Lantern Corps,</span>
      <span class="quote-line">my batchmates have always motivated me to press</span>
      <span class="quote-line">on and work hard towards every goal we set our</span>
      <span class="quote-line">sights on. It is through journeying with them and</span>
      <span class="quote-line">my Officers that I have learnt valuable lessons of</span>
      <span class="quote-line">perseverance, self-discipline, selflessness and to care</span>
      <span class="quote-line">for others. Resillience is one of the most important</span>
      <span class="quote-line">values I have gained, as the fair share od mistakes</span>
      <span class="quote-line">I made along the way taught me that the journey</span>
      <span class="quote-line">was far more important than the result because this</span>
      <span class="quote-line quote-line--last">gave us the opportunity to become better.<svg class="quote-mark quote-mark--close" viewBox="0 0 18 11"><polygon points="4,0 9,0 5,11 0,11" fill="#d9b75e"/><polygon points="13,0 18,0 14,11 9,11" fill="#d9b75e"/></svg></span>
    </p>
  </article>

  <div class="fold-line"></div>
</div>
</body>
</html>
```